1 Page Bio, describing our Mission to buy multifamily properties in Colorado Springs.

I am uploading a sample of an associate who is doing a similar thing in Tampa Florida. I will also upload an attempt by my assistant to make the flyer and I will upload 3 pictures to use, along with another document that has text to add. I want to be able to edit the document pretty easily inside a google doc. thanks, I want it to look clean and professional.

```html
<!DOCTYPE html>
<html lang="en">
<head>
<meta charset="utf-8">
<title>Cedarline Investments – One Page Bio</title>
<link href="https://fonts.googleapis.com/css2?family=Montserrat:wght@400;500;600;700&display=swap" rel="stylesheet">
<style>
  :root {
    --backdrop: #e6e6e6;
    --paper: #ffffff;
    --navy: #0f4c8a;
    --heading: #13508f;
    --sky: #9cc5e8;
    --sky-light: #dbe9f6;
    --rule: #b9d3ec;
    --ink: #2e2e2e;
    --logo-ink: #1c1c1c;
  }
  * { box-sizing: border-box; margin: 0; padding: 0; }
  html, body {
    width: 1200px; height: 2301px; overflow: hidden;
    background: var(--backdrop);
    font-family: "Montserrat", sans-serif;
    color: var(--ink);
  }
  .page {
    position: absolute; left: 40px; top: 357px;
    width: 1120px; height: 1587px;
    background: var(--paper);
    box-shadow: 0 2px 8px rgba(0,0,0,.12);
    overflow: hidden;
  }
  .hero {
    position: absolute; left: 0; top: 0; width: 100%; height: 264px;
    background:
      linear-gradient(100deg, rgba(255,255,255,.85) 0%, rgba(255,255,255,.35) 40%, rgba(255,255,255,0) 60%),
      linear-gradient(180deg, #dfe9f4 0%, #9dbde0 55%, #3f6fb0 100%);
  }
  .hero-rule {
    position: absolute; left: 0; top: 264px; width: 100%; height: 6px;
    background: var(--sky);
  }
  .brand {
    position: absolute; left: 70px; top: 80px;
    display: flex; align-items: center; gap: 16px;
    font-weight: 600; font-size: 44px; letter-spacing: 1px;
    color: var(--logo-ink);
  }
  .brand-dot { width: 46px; height: 46px; border-radius: 50%; background: var(--logo-ink); }

  .block { position: absolute; }
  .col-left { left: 70px; }
  .col-right { left: 588px; }

  .title {
    display: inline-block; position: relative;
    font-weight: 700; font-size: 23px; color: var(--heading);
    letter-spacing: .5px; padding-bottom: 14px;
  }
  .title::after {
    content: ""; position: absolute; left: 50%; bottom: 0;
    width: 46px; height: 5px; border-radius: 3px;
    background: var(--navy); transform: translateX(-50%);
  }
  .title.large { font-size: 27px; }
  .subtitle {
    display: inline-block; position: relative;
    font-weight: 600; font-size: 21px; color: var(--heading);
    padding-bottom: 12px; padding-right: 40px;
  }
  .subtitle::before {
    content: ""; position: absolute; left: 0; right: 0; bottom: 2px;
    height: 1px; background: var(--rule);
  }
  .subtitle::after {
    content: ""; position: absolute; left: 0; bottom: 0;
    width: 50px; height: 5px; border-radius: 3px; background: var(--navy);
  }
  .centered::after { left: 50%; transform: translateX(-50%); }

  .lead { font-size: 18px; line-height: 1.3; width: 440px; }

  .ticks { list-style: none; }
  .ticks li {
    position: absolute; display: flex; gap: 12px;
    font-size: 18px; line-height: 1.25; width: 440px;
  }
  .ticks svg { flex: 0 0 18px; width: 18px; height: 18px; margin-top: 2px; }

  .group-label {
    position: absolute; transform: translateX(-50%);
    font-weight: 600; font-size: 21px; color: var(--heading);
    padding-bottom: 12px; text-align: center;
  }
  .group-label::after {
    content: ""; position: absolute; left: 50%; bottom: 0;
    width: 44px; height: 5px; border-radius: 3px; background: var(--navy);
    transform: translateX(-50%);
  }
  .portrait {
    position: absolute; border-radius: 50%;
    transform: translate(-50%, -50%);
  }
  .portrait.principal {
    width: 154px; height: 154px;
    background: radial-gradient(circle at 50% 45%, #6d7a5a 0%, #485240 60%, #2d3328 100%);
    border: 3px solid var(--navy);
  }
  .portrait.advisor {
    width: 140px; height: 140px;
    background: radial-gradient(circle at 50% 40%, #c9dff2 0%, var(--sky) 75%);
    border-bottom: 5px solid var(--navy);
  }
  .caption {
    position: absolute; transform: translateX(-50%);
    font-weight: 600; font-size: 19px; color: var(--heading);
    white-space: nowrap; padding-bottom: 22px; text-align: center;
  }
  .caption::before {
    content: ""; position: absolute; left: -30px; right: -30px; bottom: 2px;
    height: 1px; background: var(--rule);
  }
  .caption::after {
    content: ""; position: absolute; left: 50%; bottom: 0;
    width: 34px; height: 5px; border-radius: 3px; background: var(--navy);
    transform: translateX(-50%);
  }
  .caption.short::before { left: -10px; right: -10px; }

  .footer {
    position: absolute; left: 0; bottom: 0; width: 100%; height: 67px;
    background: var(--navy); color: #fff; font-size: 17px;
  }
  .chevrons { position: absolute; left: 0; top: 0; height: 67px; width: 140px; }
  .contact { position: absolute; top: 22px; display: flex; align-items: center; gap: 14px; }
  .contact svg { width: 22px; height: 22px; }
</style>
</head>
<body>
<svg width="0" height="0" style="position:absolute">
  <defs>
    <symbol id="tick" viewBox="0 0 20 20">
      <path d="M17 7.5 A8 8 0 1 1 14 3.6" fill="none" stroke="#13508f" stroke-width="1.8" stroke-linecap="round"/>
      <path d="M6 10 L9.2 13 L18 4" fill="none" stroke="#13508f" stroke-width="2" stroke-linecap="round" stroke-linejoin="round"/>
    </symbol>
  </defs>
</svg>

<main class="page">
  <div class="hero" role="img" aria-label="Photo of glass office towers against a pale blue cloudy sky"></div>
  <div class="hero-rule"></div>
  <div class="brand"><span class="brand-dot"></span>Cedarline Investments</div>

  <!-- Mission column -->
  <div class="block col-left" style="top:302px"><h2 class="title">THE MISSION</h2></div>
  <p class="block col-left lead" style="top:356px">To create a family business by purchasing Multifamily Residences, one at a time.</p>
  <div class="block col-left" style="top:414px"><h3 class="subtitle">The Process</h3></div>
  <ul class="ticks">
    <li style="left:70px;top:466px"><svg><use href="#tick"/></svg>Buy right, manage right, and finance right.</li>
  </ul>
  <div class="block col-left" style="top:506px"><h3 class="subtitle">The Market</h3></div>
  <ul class="ticks">
    <li style="left:70px;top:568px"><svg><use href="#tick"/></svg>Colorado Springs</li>
    <li style="left:70px;top:603px"><svg><use href="#tick"/></svg>Projected job growth of nearly 50%</li>
    <li style="left:70px;top:639px"><svg><use href="#tick"/></svg>Solid economy, military, aerospace,<br>electronics industry, and tourism.</li>
  </ul>

  <!-- Values column -->
  <div class="block col-right" style="top:302px"><h2 class="title">VALUES</h2></div>
  <p class="block col-right lead" style="top:356px;width:490px">To provide a white glove experience to all residences with a clean, safe, and fun environment.</p>
  <div class="block col-right" style="top:418px"><h3 class="subtitle">The Target</h3></div>
  <ul class="ticks">
    <li style="left:588px;top:466px"><svg><use href="#tick"/></svg>B and C class assets located in Colorado<br>Springs or nearby submarkets.</li>
    <li style="left:588px;top:568px"><svg><use href="#tick"/></svg>Below average unemployment rates.</li>
    <li style="left:588px;top:603px"><svg><use href="#tick"/></svg>Above-average incomes.</li>
  </ul>

  <!-- Team -->
  <div class="block col-left" style="top:706px"><h2 class="title large">THE TEAM</h2></div>

  <h3 class="group-label" style="left:256px;top:784px">Principals</h3>
  <div class="portrait principal" style="left:259px;top:923px" role="img" aria-label="Portrait photo of the two principals outdoors"></div>
  <div class="caption" style="left:259px;top:1018px">Rowan &amp; Glen Albright</div>

  <h3 class="group-label" style="left:791px;top:786px">Advisors</h3>
  <div class="portrait advisor" style="left:708px;top:930px" role="img" aria-label="Headshot of advisor Owen Pratt"></div>
  <div class="portrait advisor" style="left:880px;top:930px" role="img" aria-label="Headshot of advisor Dale Summers"></div>
  <div class="caption short" style="left:708px;top:1018px">Owen Pratt</div>
  <div class="caption short" style="left:880px;top:1018px">Dale Summers</div>

  <div class="block col-left" style="top:1104px"><h3 class="subtitle">Rowan Albright</h3></div>
  <ul class="ticks">
    <li style="left:70px;top:1168px"><svg><use href="#tick"/></svg>Licensed Colorado Real Estate Agent 18<br>years.</li>
    <li style="left:70px;top:1221px"><svg><use href="#tick"/></svg>Broker-Owner of two HomeCrest Franchises<br>7 and 2 Years.</li>
    <li style="left:70px;top:1275px"><svg><use href="#tick"/></svg>Married 24 years to Marla, parenting 10<br>children together.</li>
    <li style="left:70px;top:1333px"><svg><use href="#tick"/></svg>$2M portfolio.</li>
    <li style="left:588px;top:1168px"><svg><use href="#tick"/></svg>Real Estate investing for 5 years.</li>
    <li style="left:588px;top:1221px"><svg><use href="#tick"/></svg>Member of Keystone Income Academy.</li>
    <li style="left:588px;top:1275px"><svg><use href="#tick"/></svg>Appeared on Sam and Theo's Apartment<br>Hour podcast Episode 43</li>
  </ul>

  <div class="block col-left" style="top:1378px"><h3 class="subtitle">Glen Albright</h3></div>
  <ul class="ticks">
    <li style="left:70px;top:1436px"><svg><use href="#tick"/></svg>Retired Electrical Engineer.</li>
    <li style="left:70px;top:1473px"><svg><use href="#tick"/></svg>Active Real Estate Investor/Consultant.</li>
    <li style="left:588px;top:1436px"><svg><use href="#tick"/></svg>Net worth over $4M</li>
    <li style="left:588px;top:1473px"><svg><use href="#tick"/></svg>15 Grandchildren.</li>
  </ul>

  <footer class="footer">
    <svg class="chevrons" viewBox="0 0 140 67" aria-hidden="true">
      <polygon points="0,0 40,0 72,33.5 40,67 0,67 30,33.5" fill="#bcd8f1"/>
      <polygon points="36,0 76,0 108,33.5 76,67 36,67 66,33.5" fill="#8fbde6"/>
    </svg>
    <div class="contact" style="left:337px">
      <svg viewBox="0 0 24 24" aria-hidden="true"><path d="M3 9c0-2 4-4 9-4s9 2 9 4v1h-4V8.5c-1.5-.7-3-1-5-1s-3.5.3-5 1V10H3z M6 12h12l2 8H4z" fill="#fff"/><circle cx="12" cy="16" r="2" fill="#0f4c8a"/></svg>
      719-555-0148
    </div>
    <div class="contact" style="left:580px">
      <svg viewBox="0 0 24 24" aria-hidden="true"><rect x="2" y="5" width="20" height="14" fill="#fff"/><path d="M2 5 L12 13 L22 5" fill="none" stroke="#0f4c8a" stroke-width="1.6"/></svg>
      ralbright@example.com
    </div>
  </footer>
</main>
</body>
</html>
```